Verostel business card

Business card for sustainable investment company called "Verostel". Verostel is an exchange platform selling carbon credits between buyers and sellers. Carbon Credits are an environmental commodity for reducing global carbon emissions.

the card should obviously have our logo and the theme should be sustainability/environment mixed with a trading platform.

Contact Information for Business Card

Logo, Name, Title, Phone, Email

Colors
0054AA
0677BA
7BADD7
CADEEF
E8F1F8
0094D4
00A9DD
6FCCEA
C7EBF8
E9F6FB
00AB8E
00BBA5
67D7C9
C6EFE9
E9F9F6
59FF00
82FF00
B8FF75
E3FFCB
F4FFEA

```html
<!DOCTYPE html>
<html lang="en">
<head>
<meta charset="utf-8">
<title>Verostel business card</title>
<link rel="stylesheet" href="https://fonts.googleapis.com/css2?family=Archivo:wght@600;700&family=Montserrat:wght@600&family=Oswald:wght@700&display=swap">
<style>
  :root {
    --ink: #0c0c0c;
    --paper: #ffffff;
    --edge: #b8977a;
  }
  * { margin: 0; padding: 0; box-sizing: border-box; }
  html, body { width: 1200px; height: 1200px; overflow: hidden; background: var(--paper); }
  .canvas { position: relative; width: 1200px; height: 1200px; }

  .card { position: absolute; left: 241px; width: 725px; height: 434px; background: var(--paper); }
  .card--front { top: 144px; border-left: 1px solid var(--edge); border-bottom: 2px solid var(--edge); }
  .card--back { top: 643px; border-left: 1px solid var(--edge); }

  .brand-mini {
    position: absolute; right: 46px; top: 44px;
    display: flex; align-items: center; gap: 8px;
    font-family: "Archivo", sans-serif; font-weight: 700; font-size: 20px; color: var(--ink);
  }
  .brand-mini__square { width: 16px; height: 16px; background: var(--ink); }

  .identity { position: absolute; right: 352px; top: 190px; text-align: right; color: var(--ink); }
  .identity__name {
    font-family: "Oswald", sans-serif; font-weight: 700; font-size: 44px;
    line-height: 1; letter-spacing: 2px;
  }
  .identity__title {
    font-family: "Archivo", sans-serif; font-weight: 600; font-size: 19px;
    line-height: 1; margin-top: 8px; letter-spacing: 0.5px;
  }

  .divider { position: absolute; left: 402px; top: 184px; width: 2px; height: 80px; background: var(--ink); }

  .contact { position: absolute; left: 432px; top: 188px; color: var(--ink); font-family: "Archivo", sans-serif; font-weight: 700; }
  .contact__phone { font-size: 22px; line-height: 1; letter-spacing: 0.5px; }
  .contact__line { font-size: 18px; line-height: 1; margin-top: 9px; letter-spacing: 0.4px; }
  .contact__line:nth-child(2) { margin-top: 11px; }

  .brand-large {
    position: absolute; left: 96px; top: 167px;
    display: flex; align-items: center; gap: 24px;
    font-family: "Montserrat", sans-serif; font-weight: 600; font-size: 70px;
    line-height: 1; color: var(--ink); letter-spacing: 1px;
  }
  .brand-large__square { width: 80px; height: 80px; background: var(--ink); }
</style>
</head>
<body>
<main class="canvas">
  <section class="card card--front" aria-label="Card front">
    <div class="brand-mini"><span class="brand-mini__square"></span>Verostel</div>
    <div class="identity">
      <p class="identity__name">DARA SOLTANI</p>
      <p class="identity__title">Founder</p>
    </div>
    <div class="divider"></div>
    <div class="contact">
      <p class="contact__phone">5550142837</p>
      <p class="contact__line">dara@verostel.com</p>
      <p class="contact__line">verostel.com</p>
    </div>
  </section>

  <section class="card card--back" aria-label="Card back">
    <div class="brand-large"><span class="brand-large__square"></span>VEROSTEL</div>
  </section>
</main>
</body>
</html>
```